Rabbit Meat Label

We need a label for a shrink-wrapped tray of rabbit. The label does not need to be fancy, we just want a simple sticker to show customers a mock-up of what it may look like. The label is approximately 5" x 2.75". The label will go on top of the rabbit, so it will not lay flat. Please take that into consideration

The rabbit specifically is farm raised. Whole cut-up with 2 fore-legs, 2 hind legs and back.

There is nutritional information on the back, so please mention that somewhere on the label.

Industry/Entity Type

Farm

Requirements
Must have
• Please leave spaces for KFPB seals and other misc items. They are about 0.5" squares.
Should not have
• Do not have anything like "Made in the USA" or "All Natural." This will be added later, if need be.

```html
<!DOCTYPE html>
<html lang="en">
<head>
<meta charset="utf-8">
<title>Farm Raised Rabbit Label</title>
<link rel="stylesheet" href="https://fonts.googleapis.com/css2?family=Arimo:wght@400;700&display=swap">
<style>
  :root {
    --ink: #111111;
    --meat: #7b3b3a;
    --paper: #ffffff;
    --linen: #ebe8cc;
    --linen-deep: #e2dfbf;
    --rule-dots: #a9a9a9;
  }
  html, body {
    margin: 0;
    padding: 0;
    overflow: hidden;
  }
  .label {
    position: relative;
    width: 1200px;
    height: 661px;
    background: var(--paper);
    font-family: "Arimo", Arial, sans-serif;
    color: var(--ink);
    overflow: hidden;
  }
  .label__text {
    position: absolute;
    left: 0;
    top: 0;
    width: 610px;
    height: 661px;
  }
  .rule {
    position: absolute;
    left: 64px;
    width: 469px;
    height: 5px;
    background: var(--ink);
  }
  .rule--top { top: 81px; }
  .rule--bottom { top: 494px; }
  .rule--dotted {
    top: 323px;
    height: 0;
    background: none;
    border-top: 4px dotted var(--rule-dots);
  }
  .line {
    position: absolute;
    margin: 0;
    white-space: nowrap;
    line-height: 1;
  }
  .title-origin {
    left: 64px;
    top: 110px;
    font-size: 78px;
    font-weight: 400;
    letter-spacing: 0.5px;
  }
  .title-product {
    left: 58px;
    top: 186px;
    font-size: 160px;
    font-weight: 400;
    color: var(--meat);
    letter-spacing: -1px;
  }
  .cut-heading {
    left: 64px;
    top: 339px;
    font-size: 57px;
  }
  .cut-count {
    left: 62px;
    top: 403px;
    font-size: 96px;
    color: var(--meat);
  }
  .cut-parts {
    left: 124px;
    top: 410px;
    font-size: 36px;
    line-height: 1.05;
  }
  .cut-parts span { display: block; }
  .cut-back {
    left: 300px;
    top: 420px;
    font-size: 70px;
  }
  .cut-back .amp { font-weight: 700; }
  .nutrition-note {
    left: 66px;
    top: 514px;
    font-size: 21px;
  }
  .label__art {
    position: absolute;
    left: 610px;
    top: 0;
    width: 590px;
    height: 661px;
    background: var(--linen);
  }
  .art-area {
    position: absolute;
    left: 48px;
    top: 64px;
    width: 514px;
    height: 514px;
    border-radius: 8px;
    background: radial-gradient(ellipse at 62% 55%, #a0625a 0%, var(--linen-deep) 60%, var(--linen) 100%);
  }
</style>
</head>
<body>
<main class="label">
  <section class="label__text">
    <div class="rule rule--top"></div>
    <h1 class="line title-origin">Farm Raised</h1>
    <p class="line title-product">Rabbit</p>
    <div class="rule rule--dotted"></div>
    <p class="line cut-heading">Whole cut-up with</p>
    <p class="line cut-count">2</p>
    <p class="line cut-parts"><span>forelegs</span><span>hind legs</span></p>
    <p class="line cut-back"><span class="amp">&amp;</span> back</p>
    <div class="rule rule--bottom"></div>
    <p class="line nutrition-note">See nutritional information on the back</p>
  </section>
  <section class="label__art">
    <div class="art-area" role="img" aria-label="Illustration of a sitting rabbit outlined in white, with the cuts — forelegs, hind legs and back — shaded in meat red"></div>
  </section>
</main>
</body>
</html>
```